Professionelles Design für Use Case Präsentationen im B2B-Bereich

Wir sind ein Schweizer Technologieunternehmen (Kalvor GmbH, www.kalvor.ch), das datenbasierte Simulationen, Optimierung und Entscheidungsunterstützung für Unternehmen in Logistik, Produktion und Verkehr anbietet.
Ziel dieses Projekts ist es, bestehende Use Cases in ein modernes, visuell ansprechendes Format zu bringen, das unsere Kompetenz und den Nutzen für Kunden klar kommuniziert. Die Zielgruppe sind Entscheidungsträger in mittleren bis großen Industrieunternehmen (Bereichsleiter, Projektleiter, Geschäftsleitung).
Was wir brauchen:
– Ein cleanes, professionelles Design (PowerPoint oder PDF-Layout), das sich gut für Präsentationen, Whitepaper oder als LinkedIn-Content eignet.
– Klare Struktur mit Infografiken, Icons, Diagrammen oder Visualisierungen.
– Integration unseres Logos, Farbschemas und ggf. unseres Slogans.
Stilrichtung:
– Modern, technisch fundiert, aber nicht überladen
– Klar, direkt, seriös
– Gerne mit einem visuellen roten Faden (z. B. durchgängige Icons oder Layout-Struktur)
Ein Beispieldokument (UseCase Transportkosten) mit Inhalte ist angefügt. Ziel ist eine wiederverwendbare Vorlage, die wir für verschiedene Kunden-Use-Cases adaptieren können.
- Roboto

```html
<!DOCTYPE html>
<html lang="de">
<head>
<meta charset="utf-8">
<title>Kalvor GmbH – Use Case</title>
<link rel="stylesheet" href="https://fonts.googleapis.com/css2?family=Roboto:wght@300;400;500;700&display=swap">
<style>
  :root {
    --bg: #ffffff;
    --card: #f4f4f4;
    --card-faded: #fbfbfb;
    --ink: #111111;
    --ink-faded: #c9c9c9;
    --rule: #e6e6e6;
  }
  * { box-sizing: border-box; margin: 0; padding: 0; }
  html, body { width: 1200px; height: 675px; overflow: hidden; background: var(--bg); font-family: "Roboto", sans-serif; color: var(--ink); }
  .slide { position: relative; width: 1200px; height: 675px; }
  .cards { position: absolute; top: 117px; left: 49px; display: flex; gap: 16px; }
  .card {
    width: 264px; height: 441px; border-radius: 20px; background: var(--card-faded);
    padding: 24px 0 0 25px; position: relative; overflow: hidden;
  }
  .card.is-active { background: var(--card); border: 1px solid #e2e2e2; padding: 23px 0 0 24px; }
  .step { width: 40px; height: 40px; border-radius: 50%; background: #fff; display: flex; align-items: center; justify-content: center; font-size: 20px; color: var(--ink-faded); }
  .card h2 { margin-top: 18px; font-size: 16.5px; font-weight: 500; line-height: 23px; letter-spacing: -0.2px; color: var(--ink-faded); }
  .card p { margin-top: 9px; font-size: 11.7px; line-height: 16.8px; font-weight: 300; color: var(--ink-faded); }
  .is-active .step, .is-active h2, .is-active p { color: var(--ink); }
  .is-active p { font-weight: 400; }
  .photo { position: absolute; left: 25px; right: 0; bottom: 0; height: 230px; opacity: .28; }
  .is-active .photo { left: 24px; opacity: 1; }
  .photo-1 { background: linear-gradient(135deg, #8a7f6a, #d9d2c4 60%, #bfb9ad); }
  .photo-2 { background: linear-gradient(150deg, #2d3346 0%, #6e5a45 45%, #b07a45 70%, #e3e0da 100%); }
  .photo-3 { background: linear-gradient(135deg, #6d6a66, #c9c6c0 50%, #4e4a45); }
  .photo-4 { background: linear-gradient(135deg, #e6e8ea, #bdbfc2 55%, #3a3a3c); }
  .footer { position: absolute; left: 0; right: 0; bottom: 0; height: 40px; border-top: 1px solid var(--rule); display: flex; align-items: center; justify-content: space-between; padding: 0 31px 0 50px; }
  .brand { font-size: 13px; font-weight: 700; }
  .web { font-size: 13px; font-weight: 700; }
</style>
</head>
<body>
<div class="slide">
  <div class="cards">
    <article class="card">
      <div class="step">1</div>
      <h2>Vergleich der Standorte<br>mit echten Touren</h2>
      <p>Standorte werden mit<br>realitätsnahen Touren simuliert<br>und direkt vergleichbar gemacht.</p>
      <div class="photo photo-1" role="img" aria-label="Foto: zwei Personen besprechen Ergebnisse auf einem Tablet"></div>
    </article>
    <article class="card is-active">
      <div class="step">2</div>
      <h2>Transparente Berechnung<br>der Transportkosten</h2>
      <p>Alle Transportkosten werden<br>datenbasiert, nachvollziehbar<br>und vollständig ausgewiesen.</p>
      <div class="photo photo-2" role="img" aria-label="Foto: Team analysiert Diagramme und Unterlagen auf einem Holztisch"></div>
    </article>
    <article class="card">
      <div class="step">3</div>
      <h2>Klare Entscheidungsgrundlage<br>für Geschäftsleitung</h2>
      <p>Simulation liefert fundierte<br>Ergebnisse für schnelle und<br>sichere Standortentscheidungen.</p>
      <div class="photo photo-3" role="img" aria-label="Foto: Besprechung im Team vor einem Bildschirm mit Diagrammen"></div>
    </article>
    <article class="card">
      <div class="step">4</div>
      <h2>Erste Resultate in<br>weniger als 3 Wochen</h2>
      <p>Vom Start bis zu verwertbaren<br>Ergebnissen vergehen oft<br>weniger als 21 Tage.</p>
      <div class="photo photo-4" role="img" aria-label="Foto: Präsentation von Ergebnissen an einem Whiteboard"></div>
    </article>
  </div>
  <footer class="footer">
    <div class="brand">Kalvor GmbH</div>
    <div class="web">www.kalvor.ch</div>
  </footer>
</div>
</body>
</html>
```